Congressional Website with splash page for Texas Democratic Black Woman

I would like a splash page with a turquoise shaded theme to it. My logo can be played with but the original logo is black white and red... we are now wanting a page that is in shades of turquoise with the black white and red colors. On the splash page, I want to collect volunteer information and prompt people to donate. I would like to.just have a large picture of me of some sort and then you have to click to enter the rest of the page with the issues.

Target Market(s)

Voters and Donors and democrats

Industry/Entity Type

campaign/elections

Coding

Coded - Design and coding required

Number of Pages Required

2 page

Font styles to use
Serif

Colors
0094D4
00A9DD
6FCCEA
C7EBF8
E9F6FB

Requirements
Must have
• I must have a landing page... and then it open up to the other pages.

```html
<!DOCTYPE html>
<html lang="en">
<head>
<meta charset="utf-8">
<title>Jordan Whitfield — Democrat for US Congress</title>
<link href="https://fonts.googleapis.com/css2?family=Playfair+Display:wght@400&family=Oswald:wght@500&family=Roboto:wght@400;700&display=swap" rel="stylesheet">
<style>
  :root {
    --teal-deep: #2f8f95;
    --teal: #4aa9ad;
    --teal-soft: #6fbfc0;
    --stone: #8f8580;
    --stone-light: #b9aaa4;
    --white: #ffffff;
    --red: #ff0022;
    --red-dark: #f20d2a;
    --ink: #222222;
  }
  * { box-sizing: border-box; margin: 0; padding: 0; }
  html, body { width: 1200px; height: 953px; overflow: hidden; }
  body { font-family: "Roboto", Arial, sans-serif; color: var(--white); background: var(--white); }

  .hero { position: relative; width: 1200px; height: 733px; overflow: hidden; }
  .hero-photo {
    position: absolute; inset: 0;
    background:
      linear-gradient(90deg, var(--teal) 0%, var(--teal-soft) 35%, rgba(111,191,192,0.6) 48%, rgba(143,133,128,0) 62%),
      linear-gradient(90deg, var(--teal-deep) 0%, #5b6f70 55%, var(--stone) 80%, var(--stone-light) 100%);
  }
  .hero-photo .portrait {
    position: absolute; left: 520px; top: 60px; width: 620px; height: 673px;
    background: radial-gradient(ellipse at 50% 60%, #2a2b33 0%, #2c2e36 55%, rgba(44,46,54,0) 75%);
  }

  .brand { position: absolute; left: 47px; top: 30px; width: 296px; }
  .brand-name {
    font-family: "Playfair Display", Georgia, serif; font-weight: 400;
    font-size: 40px; line-height: 1; letter-spacing: 1px; white-space: nowrap;
    padding-bottom: 14px;
  }
  .brand-tag {
    border-top: 3px solid var(--white); border-bottom: 3px solid var(--white);
    font-family: "Oswald", Impact, sans-serif; font-weight: 500;
    font-size: 21px; letter-spacing: 1.6px; text-align: center;
    padding: 4px 0 3px;
  }

  .headline {
    position: absolute; left: 45px; top: 226px; width: 480px;
    font-family: "Playfair Display", Georgia, serif; font-weight: 400;
    font-size: 50px; line-height: 48px;
  }

  .signup { position: absolute; left: 44px; top: 443px; }
  .field-labels { display: flex; font-size: 15px; margin-bottom: 8px; }
  .field-labels span:first-child { width: 298px; padding-left: 2px; }
  .fields { display: flex; gap: 9px; }
  .field {
    height: 41px; background: var(--white); border-radius: 2px;
    color: var(--ink); font-size: 13px; padding: 13px 12px;
  }
  .field-email { width: 289px; }
  .field-zip { width: 151px; }
  .btn-join {
    margin-top: 14px; width: 167px; height: 49px; background: var(--red);
    border-radius: 2px; font-weight: 700; font-size: 17px; text-align: center; line-height: 49px;
  }

  .next-steps { position: absolute; left: 44px; top: 604px; display: flex; align-items: center; }
  .btn { height: 49px; border-radius: 2px; font-weight: 700; font-size: 15px;
         display: flex; align-items: center; justify-content: center; gap: 5px; }
  .btn-resources { width: 198px; background: var(--white); color: var(--red); }
  .btn-site { width: 179px; border: 1.5px solid var(--white); color: var(--white); }
  .or { width: 58px; text-align: center; font-size: 15px; }
  .btn svg { width: 6px; height: 9px; }

  .footer-contact {
    height: 136px; background: var(--red); display: flex; padding-top: 45px; font-size: 16px; line-height: 23px;
  }
  .footer-contact .col { position: absolute; text-align: center; transform: translateX(-50%); }
  .footer-contact strong { font-weight: 700; font-size: 18px; }
  .footer-note {
    height: 84px; background: var(--red-dark); text-align: center;
    font-size: 19px; line-height: 23px; padding-top: 18px;
  }
  .footer-note a { color: var(--white); font-weight: 700; text-decoration: underline; }
</style>
</head>
<body>
  <section class="hero">
    <div class="hero-photo" role="img" aria-label="Portrait of the candidate in a dark suit standing between stone columns, tinted turquoise on the left">
      <div class="portrait"></div>
    </div>

    <header class="brand">
      <div class="brand-name">JORDAN WHITFIELD</div>
      <div class="brand-tag">DEMOCRAT FOR US CONGRESS</div>
    </header>

    <h1 class="headline">The fight for social, racial, and economic justice has never been more urgent.</h1>

    <form class="signup">
      <div class="field-labels"><span>EMAIL ADDRESS</span><span>ZIP CODE</span></div>
      <div class="fields">
        <div class="field field-email">Email</div>
        <div class="field field-zip">Zip*</div>
      </div>
      <div class="btn-join">JOIN US</div>
    </form>

    <nav class="next-steps">
      <div class="btn btn-resources">COVID-19 RESOURCES
        <svg viewBox="0 0 6 9"><path d="M0 0 L6 4.5 L0 9 Z" fill="currentColor"/></svg></div>
      <div class="or">-OR-</div>
      <div class="btn btn-site">CONTINUE TO SITE
        <svg viewBox="0 0 6 9"><path d="M0 0 L6 4.5 L0 9 Z" fill="currentColor"/></svg></div>
    </nav>
  </section>

  <footer>
    <div class="footer-contact">
      <div class="col" style="left:298px">General Contact:<br><strong>info@JordanWhitfield.com</strong></div>
      <div class="col" style="left:666px">Call: <strong>(555) 010-2040</strong><br>Jordan Whitfield</div>
      <div class="col" style="left:967px">Accessibility<br>Privacy Policy</div>
    </div>
    <div class="footer-note">
      Thank you for visiting my campaign website. If your intention was to visit my official House<br>
      of Representatives website, please <a href="#">click here.</a>
    </div>
  </footer>
</body>
</html>
```